Flyer-Design für Immobilienhändler
Zielgruppe
Ich bin ein kleiner Immobilienhändler (nebenberuflich, meine Frau und ich, 2-Mann Unternehmen) und kaufe direkt Wohnimmobilen (Haus/Wohnungen) ein, um diese aufzuwerten und dann wieder zu verkaufen. Ich bin kein Makler, habe aber ähnliche Zielgruppen wie ein Makler, nur mit dem Unterschied das ich die Immos direkt kostenfrei kaufe so wie sie sind! Zielgruppe sind bei mir Privatpersonen (im mittlerem-höherem Alter 50-80 Jahre) die Ihre Immobilie verkaufen möchten.
Aufgabenstellung
Es soll ein Flyer sein mit folgenden Vorgaben:
• Design: Modern, einfach und wichtig ist das es professional und sehr seriös wirkt
• Auf den ersten Blick sollte die Message verständlich sein was ich suche und was die Vorteile sind es bei mir zu verkaufen, anstatt das einem Makler zu übergeben (siehe mein Entwurf).
• Flyer Format z.B. DIN A5/A6, was sich gut versenden lässt. Vorschläge sind willkommen
Im Anhang habe ein einen eigenen Entwurf beigefügt, jedoch bin offen für komplett neue Vorschläge was Text und Design angeht.

```html
<!DOCTYPE html>
<html lang="de">
<head>
<meta charset="utf-8">
<title>Flyer Immobilienankauf – Außen- und Innenseite</title>
<link rel="stylesheet" href="https://fonts.googleapis.com/css2?family=Ubuntu:wght@500;700&family=Roboto+Condensed:wght@400;700&display=swap">
<style>
  :root {
    --yellow: #fccb27;
    --yellow-deep: #f2bd1a;
    --blue: #1a9ad8;
    --ink: #1e1e1e;
    --white: #ffffff;
    --page: #ffffff;
    --photo-green: #b7cf8a;
    --photo-sky: #dfe9d2;
    --photo-grey: #dcdedf;
  }
  * { box-sizing: border-box; margin: 0; padding: 0; }
  html, body { width: 1200px; height: 2400px; overflow: hidden; background: var(--page); }
  body { position: relative; font-family: "Roboto Condensed", "Arial Narrow", sans-serif; color: var(--ink); }

  .spread {
    position: absolute; left: 100px; width: 1000px; height: 351px;
    display: flex; box-shadow: 0 3px 10px rgba(0,0,0,.28);
  }
  .spread--outside { top: 860px; }
  .spread--inside { top: 1300px; }
  .panel { position: relative; width: 500px; height: 100%; overflow: hidden; }
  .panel--yellow { background: var(--yellow); }
  .panel--white { background: var(--white); }

  /* Cover */
  .cover-photo {
    position: absolute; left: 0; top: 0; width: 493px; height: 284px;
    background: linear-gradient(115deg, var(--photo-sky) 0%, var(--photo-green) 35%, #c9b6a0 62%, #e9dccd 80%, #8da7c6 100%);
  }
  .cover-rule { position: absolute; left: 0; top: 284px; width: 493px; height: 2px; background: #6d7fa1; }
  .cover-headline {
    position: absolute; left: 34px; top: 30px;
    font-family: "Ubuntu", sans-serif; font-weight: 700; font-size: 16.5px; line-height: 19px; color: var(--ink);
  }
  .benefit-tags { position: absolute; left: 34px; top: 113px; list-style: none; }
  .benefit-tags li {
    display: flex; align-items: center; gap: 6px;
    width: 164px; height: 15px; margin-bottom: 9px; padding-left: 2px;
    background: var(--yellow); font-size: 9px; font-weight: 700; color: var(--ink);
  }
  .tick { width: 12px; height: 12px; flex: none; }

  .call-badge {
    position: absolute; width: 96px; height: 96px; border-radius: 50%;
    background: var(--blue); color: var(--white);
    display: flex; flex-direction: column; justify-content: center; padding-left: 12px;
    font-family: "Ubuntu", sans-serif; font-weight: 700; font-size: 10.5px; line-height: 12px;
    transform: rotate(-12deg);
  }
  .call-badge .phone { margin-top: 4px; font-size: 9.5px; letter-spacing: .8px; }
  .spread--outside .call-badge { left: 342px; top: 228px; }
  .spread--inside .call-badge { left: 375px; top: 212px; }

  .web { position: absolute; font-size: 8px; font-weight: 700; color: var(--ink); }
  .spread--outside .web { left: 39px; top: 329px; }
  .spread--inside .web { right: 15px; top: 331px; }

  /* Back cover */
  .contact { position: absolute; left: 50px; top: 34px; width: 420px; }
  .contact h2 { font-family: "Ubuntu", sans-serif; font-weight: 700; font-size: 15px; margin-bottom: 40px; }
  .contact p { font-size: 8.5px; line-height: 12px; }
  .contact dl { margin-top: 16px; font-size: 9px; font-weight: 700; line-height: 14px; display: grid; grid-template-columns: 40px auto; }
  .brand { position: absolute; left: 60px; top: 270px; display: flex; align-items: center; gap: 6px;
    font-family: "Ubuntu", sans-serif; font-weight: 700; font-size: 14px; color: #2c3d63; }
  .brand-square { width: 14px; height: 14px; background: #2c3d63; }

  /* Inside left */
  .letter-photo {
    position: absolute; left: 17px; top: 17px; width: 461px; height: 294px;
    background: linear-gradient(90deg, #eeeff0 0%, #e3e5e6 55%, #cfd2d4 75%, var(--photo-grey) 100%);
  }
  .letter { position: absolute; left: 30px; top: 36px; width: 290px; }
  .letter h2 {
    font-family: "Ubuntu", sans-serif; font-weight: 700; font-size: 14.5px; line-height: 23px;
  }
  .letter h2 span { background: var(--yellow); padding: 0 4px; }
  .letter p { font-size: 9px; line-height: 12.5px; margin-top: 12px; }
  .signature { display: block; width: 96px; height: 22px; margin-top: 6px; background: #c9cccf; }

  /* Inside right */
  .advantages { position: absolute; left: 50px; top: 44px; width: 430px; }
  .advantages h2 { font-family: "Ubuntu", sans-serif; font-weight: 700; font-size: 14px; line-height: 17px; }
  .advantages ol { margin-top: 30px; padding-left: 14px; font-size: 10.5px; line-height: 23px; }
  .advantages ol li { padding-left: 2px; }
  .advantages .cont { display: block; line-height: 13px; margin-top: -5px; }
</style>
</head>
<body>

<section class="spread spread--outside" aria-label="Flyer Außenseite">
  <div class="panel panel--yellow cover">
    <div class="cover-photo" role="img" aria-label="Foto: lachendes älteres Paar im Grünen"></div>
    <div class="cover-rule"></div>
    <h1 class="cover-headline">Beste Aussichten für<br>Ihren Immobilienverkauf –<br>und den besten Preis.</h1>
    <ul class="benefit-tags">
      <li><svg class="tick" viewBox="0 0 12 12"><circle cx="6" cy="6" r="5" fill="none" stroke="#1e1e1e" stroke-width="1.2"/><path d="M3.5 6.2l1.8 1.7 3.3-3.6" fill="none" stroke="#1e1e1e" stroke-width="1.3"/></svg>keine Renovierung/Sanierung</li>
      <li><svg class="tick" viewBox="0 0 12 12"><circle cx="6" cy="6" r="5" fill="none" stroke="#1e1e1e" stroke-width="1.2"/><path d="M3.5 6.2l1.8 1.7 3.3-3.6" fill="none" stroke="#1e1e1e" stroke-width="1.3"/></svg>kein Besichtigungsstress</li>
      <li><svg class="tick" viewBox="0 0 12 12"><circle cx="6" cy="6" r="5" fill="none" stroke="#1e1e1e" stroke-width="1.2"/><path d="M3.5 6.2l1.8 1.7 3.3-3.6" fill="none" stroke="#1e1e1e" stroke-width="1.3"/></svg>keine Gebühren</li>
    </ul>
    <div class="call-badge">Jetzt völlig<br>unverbindlich<br>anfragen:<span class="phone">06031/482715</span></div>
    <span class="web">www.hauswert-direkt.net</span>
  </div>
  <div class="panel panel--yellow back">
    <div class="contact">
      <h2>Wenn es um Immobilienverkauf geht.</h2>
      <p>Sie wünschen ein unverbindliches Angebot?<br>Schreiben Sie uns oder rufen Sie an, völlig unverbindlich und ohne Risiko:</p>
      <dl><dt>Telefon:</dt><dd>06031 / 48 27 15</dd><dt>E-Mail:</dt><dd>kt@hauswert-direkt.net</dd></dl>
    </div>
    <div class="brand"><span class="brand-square"></span>HAUSWERT</div>
  </div>
</section>

<section class="spread spread--inside" aria-label="Flyer Innenseite">
  <div class="panel panel--white">
    <div class="letter-photo" role="img" aria-label="Foto: Porträt des Inhabers mit Brille vor hellem Hintergrund"></div>
    <div class="letter">
      <h2><span>Verkaufen ist Vertrauenssache.</span><br><span>Gerne stellen wir uns kurz vor:</span></h2>
      <p>Als Familienunternehmen aus dem Rhein-Main-Gebiet haben wir uns darauf spezialisiert, gute und solide Immobilien zu kaufen. Direkt von den Eigentümern. <b>Ohne Renovierung. Ohne Sanierung. Ohne Belästigung durch Besichtigungen</b> für Sie.</p>
      <p>Da wir <b>keine Makler</b> sind, fallen für Sie <b>keinerlei Gebühren</b> an – den <b>Bestpreis</b> zahlen wir Ihnen dennoch.</p>
      <p>Gespannt, was wir Ihnen für Ihre Immobilie zahlen?<br>Wir freuen uns auf Ihre Anfrage!</p>
      <p>Herzliche Grüße,<span class="signature" role="img" aria-label="Unterschrift von Martin Lorenz"></span></p>
    </div>
    <span class="web">www.hauswert-direkt.net</span>
  </div>
  <div class="panel panel--yellow">
    <div class="advantages">
      <h2>6 Vielversprechende Vorteile, warum wir<br>der richtige Partner für Ihren Verkauf sind:</h2>
      <ol>
        <li>Abkauf direkt von uns, zum <b>fairen Bestpreis</b></li>
        <li>Professionelle, schnelle und <b>komplette Kaufabwicklung</b> aus einer Hand</li>
        <li>Sie brauchen nicht renovieren, sanieren oder entrümpeln</li>
        <li>Sie zahlen <b>keine Maklergebühr,</b></li>
        <li>Sie haben <b>keinerlei Besucherstress</b></li>
        <li>Sie gehen <b>kein Haftungsrisiko</b> ein –<span class="cont">wir kaufen Ihre Immobilie so wie sie ist</span></li>
      </ol>
    </div>
    <div class="call-badge">Jetzt völlig<br>unverbindlich<br>anfragen:<span class="phone">06031/482715</span></div>
  </div>
</section>

</body>
</html>
```